Finiding oppertunites in Real Estate 6.15.20

size of ad 7” x 9.6”
1-I like the ad to stand out and attract people's attention.
2-you should be able to see the text of the ad clearly .. see the attachment anything in yellow is instructions.
3-the list of topics should not be the main part of the ad
4-if you decide you want a picture or vector of a person .. (you decide)
then it should be a white male about 25-30 years old wearing a solid white or blue shirt and not long hair.
5-leave 1 inch for footer
see attachment
Good luck

Target Market(s)

potential male students 25-35 years of age

Industry/Entity Type

Education

Requirements
Must have
• will stand out and people would want to see it.
should be able to read the words of ad
Nice to have
• how to make money in real estate on one line

```html
<!DOCTYPE html>
<html lang="en">
<head>
<meta charset="utf-8">
<title>Real Estate Career Course</title>
<link rel="stylesheet" href="https://fonts.googleapis.com/css2?family=Bebas+Neue&family=Montserrat:wght@800&family=Mulish:wght@500;600&display=swap">
<style>
  :root {
    --stage: #c9c9c9;
    --blue: #1c9ad9;
    --blue-deep: #078bd3;
    --blue-title: #1187d3;
    --footer: #1588c7;
    --white: #ffffff;
    --ink: #0b0b0b;
    --figure-light: #dfe3e8;
    --figure-dark: #1f2630;
  }
  * { margin: 0; padding: 0; box-sizing: border-box; }
  html, body { width: 1200px; height: 615px; overflow: hidden; background: var(--stage); }
  .flyer {
    position: absolute; left: 396px; top: 27px;
    width: 410px; height: 562px; overflow: hidden;
    background: linear-gradient(180deg, var(--blue-deep) 0%, var(--blue) 45%, var(--blue) 100%);
    font-family: "Mulish", sans-serif; color: var(--white);
  }
  .backdrop-scene {
    position: absolute; left: 120px; top: 220px; width: 290px; height: 284px;
    background: radial-gradient(ellipse at 40% 30%, rgba(255,255,255,0.10), rgba(255,255,255,0) 70%);
  }
  .title-disc { position: absolute; left: 0; top: 0; width: 410px; height: 562px; }
  .title { position: absolute; left: 22px; top: 20px; font-family: "Bebas Neue", sans-serif; font-weight: 400; line-height: 0.92; }
  .title-kicker { display: block; font-size: 29px; color: var(--ink); }
  .title-main { display: block; font-size: 49px; color: var(--blue-title); }
  .intro { position: absolute; left: 203px; top: 24px; width: 178px; list-style: none; font-size: 8px; font-weight: 500; line-height: 10.5px; }
  .intro li { position: relative; padding-left: 10px; margin-bottom: 5px; }
  .intro li::before { content: ""; position: absolute; left: 0; top: 3.5px; width: 3.5px; height: 3.5px; border-radius: 50%; background: var(--ink); }
  .sessions { position: absolute; left: 203px; top: 100px; font-family: "Bebas Neue", sans-serif; font-weight: 400; font-size: 33px; color: var(--ink); letter-spacing: -0.2px;
    text-shadow: 1px 0 var(--white), -1px 0 var(--white), 0 1px var(--white), 0 -1px var(--white), 1px 1px var(--white), -1px -1px var(--white), 1px -1px var(--white), -1px 1px var(--white); }
  .sessions-rule { position: absolute; left: 204px; top: 140px; width: 183px; height: 1.5px; background: var(--white); }
  .schedule { position: absolute; left: 204px; top: 148px; font-family: "Montserrat", sans-serif; font-weight: 800; font-size: 14px; line-height: 19.5px; }
  .schedule .date { color: var(--ink); }
  .topics-heading { position: absolute; left: 22px; top: 183px; font-family: "Bebas Neue", sans-serif; font-weight: 400; font-size: 24px; line-height: 0.95; color: var(--ink); }
  .topics { position: absolute; left: 24px; top: 235px; list-style: none; font-size: 9.5px; font-weight: 500; }
  .topics li { display: flex; align-items: center; height: 19.5px; }
  .topic-icon { width: 13px; height: 13px; border-radius: 50%; background: var(--white); margin-right: 6px; display: flex; align-items: center; justify-content: center; }
  .topic-icon::after { content: ""; width: 5px; height: 5px; border-radius: 1px; background: var(--ink); }
  .presenter {
    position: absolute; left: 238px; top: 218px; width: 132px; height: 280px; border-radius: 60px 60px 12px 12px;
    background: linear-gradient(180deg, var(--figure-light) 0%, var(--figure-light) 48%, var(--figure-dark) 56%, var(--figure-dark) 100%);
    opacity: 0.9;
  }
  .footer-space { position: absolute; left: 0; bottom: 0; width: 410px; height: 58px; background: var(--footer); }
</style>
</head>
<body>
  <main class="flyer">
    <div class="backdrop-scene" role="img" aria-label="Faded photo of a modern house behind the presenter"></div>
    <svg class="title-disc" viewBox="0 0 410 562" aria-hidden="true">
      <circle cx="60" cy="40.5" r="130.5" fill="#ffffff" stroke="#0b0b0b" stroke-width="2.5"/>
    </svg>
    <h1 class="title">
      <span class="title-kicker">Real Estate</span>
      <span class="title-main">Career</span>
      <span class="title-main">Course</span>
    </h1>
    <ul class="intro">
      <li>How to Make Money In Real Estate?</li>
      <li>An investment in knowledge opens up untold opportunities</li>
      <li>For those who have started or would like to go into Real Estate</li>
    </ul>
    <h2 class="sessions">Remote Sessions</h2>
    <div class="sessions-rule"></div>
    <p class="schedule">12 SESSION COURSE<br>CLASSES STARTING<br><span class="date">JUNE 16</span></p>
    <h3 class="topics-heading">A Partial Listing<br>of Topics</h3>
    <ul class="topics">
      <li><span class="topic-icon"></span>Single-family</li>
      <li><span class="topic-icon"></span>Multifamily</li>
      <li><span class="topic-icon"></span>Management</li>
      <li><span class="topic-icon"></span>Real Estate Concepts</li>
      <li><span class="topic-icon"></span>Real Estate law</li>
      <li><span class="topic-icon"></span>Investment properties</li>
      <li><span class="topic-icon"></span>Foreclosures</li>
      <li><span class="topic-icon"></span>Rehab</li>
      <li><span class="topic-icon"></span>Short sales</li>
      <li><span class="topic-icon"></span>Development</li>
      <li><span class="topic-icon"></span>Finical modeling</li>
      <li><span class="topic-icon"></span>HUD properties</li>
      <li><span class="topic-icon"></span>Due Diligence</li>
    </ul>
    <div class="presenter" role="img" aria-label="Illustrated young man in a white jacket, tie and black trousers, gesturing toward the text"></div>
    <div class="footer-space" aria-hidden="true"></div>
  </main>
</body>
</html>
```